Property Management Company Business Cards

Need business cards for a property management company located in Michigan. We manage houses for clients all over the world. Young and modern company, looking for eye catching design. Please work with the attached logo.

Industry/Entity Type

Property Management

Requirements
Must have
• Need lines for address, telephone number, fax number, web site.

Also lines for name, and job title

```html
<!DOCTYPE html>
<html lang="en">
<head>
<meta charset="utf-8">
<title>Northvale Estate Management – Business Card</title>
<link rel="stylesheet" href="https://fonts.googleapis.com/css2?family=Montserrat:wght@700&family=Questrial&display=swap">
<style>
  :root {
    --ink: #0a0a0a;
    --paper: #ffffff;
    --accent: #48daff;
    --accent-faint: #d3f4fd;
    --band: #000000;
  }
  html, body {
    margin: 0;
    padding: 0;
    overflow: hidden;
    background: var(--paper);
  }
  .card-sheet {
    position: relative;
    width: 982px;
    height: 1200px;
    box-sizing: border-box;
    border: 2px solid var(--ink);
    background: var(--paper);
    overflow: hidden;
    font-family: "Montserrat", sans-serif;
    color: var(--ink);
  }

  /* Front side */
  .card-front {
    position: absolute;
    left: 0; top: 0;
    width: 100%;
    height: 544px;
  }
  .brand-dot {
    position: absolute;
    left: 386px; top: 70px;
    width: 206px; height: 206px;
    border-radius: 50%;
    background: var(--accent);
  }
  .brand-name {
    position: absolute;
    left: 0; right: 0;
    top: 340px;
    margin: 0;
    text-align: center;
    font-weight: 700;
    font-size: 58px;
    line-height: 1.12;
    letter-spacing: -1px;
    color: var(--ink);
    text-transform: uppercase;
  }

  /* Divider band */
  .side-band {
    position: absolute;
    left: 0; top: 544px;
    width: 100%;
    height: 110px;
    background: var(--band);
    color: var(--paper);
    font-family: "Questrial", sans-serif;
    font-size: 48px;
  }
  .side-label {
    position: absolute;
    top: 18px;
    display: flex;
    align-items: center;
    gap: 10px;
  }
  .side-label--front { left: 262px; }
  .side-label--back { left: 567px; }
  .side-label svg { display: block; }

  /* Back side */
  .card-back {
    position: absolute;
    left: 0; top: 654px;
    width: 100%;
    height: 546px;
  }
  .back-mark {
    position: absolute;
    left: 410px; top: 22px;
    width: 500px; height: 500px;
    border-radius: 50%;
    background: var(--accent-faint);
    opacity: 0.7;
  }
  .contact {
    position: absolute;
    left: 62px; top: 62px;
  }
  .contact-name {
    margin: 0;
    font-size: 47px;
    line-height: 1;
    font-weight: 700;
  }
  .contact-title {
    margin: 14px 0 0;
    font-size: 34px;
    line-height: 1;
    font-weight: 700;
    color: var(--accent);
    text-transform: uppercase;
    letter-spacing: -0.5px;
  }
  .contact-lines {
    margin: 64px 0 0;
    padding: 0;
    list-style: none;
    font-size: 37px;
    font-weight: 700;
    line-height: 51px;
  }
  .contact-value {
    font-family: "Questrial", sans-serif;
    font-weight: 400;
    font-size: 42px;
    color: var(--accent);
  }
  .website {
    position: absolute;
    left: 187px; top: 450px;
    margin: 0;
    font-size: 41px;
    font-weight: 700;
    letter-spacing: 0.5px;
  }
</style>
</head>
<body>
<main class="card-sheet">
  <section class="card-front" aria-label="Front of card">
    <div class="brand-dot" aria-hidden="true"></div>
    <h1 class="brand-name">Northvale Estate<br>Management</h1>
  </section>

  <div class="side-band">
    <span class="side-label side-label--front">
      <svg width="24" height="66" viewBox="0 0 24 66" aria-hidden="true">
        <line x1="12" y1="8" x2="12" y2="66" stroke="#fff" stroke-width="3"/>
        <polygon points="12,0 2,18 22,18" fill="#fff"/>
      </svg>
      front
    </span>
    <span class="side-label side-label--back">
      back
      <svg width="24" height="66" viewBox="0 0 24 66" aria-hidden="true">
        <line x1="12" y1="0" x2="12" y2="58" stroke="#fff" stroke-width="3"/>
        <polygon points="12,66 2,48 22,48" fill="#fff"/>
      </svg>
    </span>
  </div>

  <section class="card-back" aria-label="Back of card">
    <div class="back-mark" aria-hidden="true"></div>
    <div class="contact">
      <p class="contact-name">John Doe</p>
      <p class="contact-title">Managing Director</p>
      <ul class="contact-lines">
        <li>Address line example 12</li>
        <li>telephone: <span class="contact-value">012 345 6789</span></li>
        <li>fax: <span class="contact-value">012 345 6789</span></li>
      </ul>
    </div>
    <p class="website">www.northvaleestates.com</p>
  </section>
</main>
</body>
</html>
```